Bottle label design for a mulberry brandy

Please create a label design for a mulberry brandy. The registered brand name is "Kolvat"
The brandy will be produced in Armenia from 100% mulberry.
Color of the product: transparent.
The product will be sold worldwide. The price will be between 30 and 50 USD. So the product will be in premium category.
Therefore we need a solid design, appropriate to the product price category. The design, however, needs to be modern and optimistic.
You can have mulberries on the label or not have, it is up to you.
We have chosen for the product some bottle types, the links to the available bottles you can find in the attachment. Ideally you show a picture of your label on the bottle you selected.

Target Market(s)

worldwide

```html
<!DOCTYPE html>
<html lang="en">
<head>
<meta charset="utf-8">
<title>Kolvat Armenian Mulberry Brandy – Label</title>
<link rel="stylesheet" href="https://fonts.googleapis.com/css2?family=Marcellus+SC&family=Montserrat:wght@600;700&display=swap">
<style>
  :root {
    --paper: #ffffff;
    --plum: #3b1654;
    --plum-deep: #2c0f40;
    --plum-soft: #5a2e78;
    --silver-light: #d9dcde;
    --silver: #a9aeb2;
    --silver-dark: #7d8388;
    --cream: #e8e5e0;
    --ink: #1d1d1f;
  }
  html, body {
    margin: 0;
    padding: 0;
    width: 1200px;
    height: 1200px;
    overflow: hidden;
    background: var(--paper);
  }
  .canvas {
    position: relative;
    width: 1200px;
    height: 1200px;
  }
  .front-label {
    position: absolute;
    left: 200px;
    top: 250px;
    width: 640px;
    height: 760px;
  }
  .neck-label {
    position: absolute;
    left: 910px;
    top: 330px;
    width: 170px;
    height: 440px;
  }
  .brand-name {
    font-family: "Marcellus SC", serif;
    font-size: 82px;
    letter-spacing: 6px;
    fill: var(--cream);
  }
  .origin {
    font-family: "Marcellus SC", serif;
    font-size: 30px;
    letter-spacing: 10px;
    fill: var(--silver);
  }
  .product-type {
    font-family: "Marcellus SC", serif;
    font-size: 42px;
    letter-spacing: 7px;
    fill: var(--cream);
  }
  .neck-claim {
    font-family: "Montserrat", sans-serif;
    font-weight: 700;
    fill: var(--ink);
  }
  .neck-percent {
    font-family: "Marcellus SC", serif;
    font-size: 34px;
    fill: var(--plum);
  }
  .neck-fruit {
    font-family: "Montserrat", sans-serif;
    font-weight: 700;
    font-size: 11px;
    fill: var(--plum);
  }
</style>
</head>
<body>
<main class="canvas">

  <svg class="front-label" viewBox="0 0 640 760" xmlns="http://www.w3.org/2000/svg">
    <defs>
      <linearGradient id="silverSheen" x1="0" y1="0" x2="1" y2="1">
        <stop offset="0" stop-color="var(--silver-light)"/>
        <stop offset="0.5" stop-color="var(--silver)"/>
        <stop offset="1" stop-color="var(--silver-dark)"/>
      </linearGradient>
      <radialGradient id="medallionTone" cx="0.5" cy="0.5" r="0.5">
        <stop offset="0" stop-color="#7a4c9a"/>
        <stop offset="1" stop-color="var(--plum-soft)"/>
      </radialGradient>
      <path id="brandArc" d="M 120,470 A 200,200 0 0 1 520,470"/>
      <path id="originArc" d="M 158,470 A 162,162 0 0 0 482,470"/>
      <path id="productArc" d="M 92,470 A 228,228 0 0 0 548,470"/>
    </defs>

    <path class="leaf-crown" role="img" aria-label="Silver ornament of mulberry clusters and leaves"
          d="M 60,230 C 110,150 220,110 320,150 C 420,110 530,150 580,230 C 520,200 440,195 380,215 C 350,200 290,200 260,215 C 200,195 120,200 60,230 Z"
          fill="url(#silverSheen)" opacity="0.85"/>

    <circle class="label-disc" cx="320" cy="470" r="262" fill="var(--plum)"/>

    <text class="brand-name" text-anchor="middle">
      <textPath href="#brandArc" startOffset="50%">KOLVAT</textPath>
    </text>

    <circle class="medallion-ring" cx="320" cy="470" r="120" fill="none" stroke="url(#silverSheen)" stroke-width="10"/>
    <circle class="medallion" role="img" aria-label="Engraved circular Armenian ornament medallion"
            cx="320" cy="470" r="114" fill="url(#medallionTone)"/>

    <text class="origin" text-anchor="middle">
      <textPath href="#originArc" startOffset="50%">ARMENIAN</textPath>
    </text>
    <text class="product-type" text-anchor="middle">
      <textPath href="#productArc" startOffset="50%">MULBERRY BRANDY</textPath>
    </text>
  </svg>

  <svg class="neck-label" viewBox="0 0 170 440" xmlns="http://www.w3.org/2000/svg">
    <rect class="neck-cap" x="0" y="0" width="170" height="80" rx="10" fill="url(#capSheen)"/>
    <defs>
      <linearGradient id="capSheen" x1="0" y1="0" x2="1" y2="0">
        <stop offset="0" stop-color="var(--silver)"/>
        <stop offset="0.5" stop-color="var(--silver-light)"/>
        <stop offset="1" stop-color="var(--silver)"/>
      </linearGradient>
    </defs>
    <path class="neck-strip" d="M 40,0 L 130,0 L 130,300 L 145,320 L 140,390 L 85,420 L 30,390 L 25,320 L 40,300 Z"
          fill="var(--cream)" stroke="var(--silver)" stroke-width="3"/>
    <rect x="55" y="40" width="60" height="250" rx="6" fill="none" stroke="var(--silver)" stroke-width="2"/>
    <text class="neck-claim" transform="translate(80,265) rotate(-90)" font-size="15" letter-spacing="3">HIGH QUALITY</text>
    <text class="neck-claim" transform="translate(98,272) rotate(-90)" font-size="12">ARMENIAN BRANDY</text>
    <text class="neck-percent" x="85" y="368" text-anchor="middle">100%</text>
    <text class="neck-fruit" x="85" y="388" text-anchor="middle">MULBERRY</text>
  </svg>

</main>
</body>
</html>
```